Acupuncture Medspa needs a business card design

I need a business card design that looks professional, has a spa-like quality and can offer a promo on the back. Initial promo is "First session free". The tagline of NeedleNook is: Refresh, Restore, Rejuvenate.

NeedleNook is a membership-based acupuncture medspa that offers acupuncture, cupping, and herbal therapies. Members choose between the "Refresh" membership which is for stress relief, or "Restore" which is for treating health conditions, and lastly "Rejuvenate" which is for natural facial enhancement.

Industry/Entity Type

Health And Wellness

Contact Information for Business Card

Coral Haskins, MAC, L.Ac.
612-555-0193
www.needlenook-example.com

Font styles to use
Serif
Sans Serif

Colors

Designer to choose colors to be used in the design.

Requirements
Must have
• The project must have NeedleNook logo, promo on the back, and contact information
Nice to have
• I would like to see the colors of the logo used.

```html
<!DOCTYPE html>
<html lang="en">
<head>
<meta charset="utf-8">
<title>NeedleNook Business Card</title>
<link href="https://fonts.googleapis.com/css2?family=Poppins:wght@400;500;600&family=Yellowtail&display=swap" rel="stylesheet">
<style>
  :root {
    --teal: #3d8783;
    --teal-bright: #2f8f88;
    --teal-soft: #cfe3e1;
    --brown-top: #4c2e14;
    --brown-bottom: #40230c;
    --white: #ffffff;
    --canvas: #e4e4e4;
  }
  * { margin: 0; padding: 0; box-sizing: border-box; }
  html, body {
    width: 1200px; height: 1200px; overflow: hidden;
    background: var(--canvas);
    font-family: "Poppins", sans-serif;
  }
  .card {
    position: absolute;
    left: 200px;
    width: 800px; height: 457px;
    border-radius: 26px;
    overflow: hidden;
  }
  .card-front { top: 80px; background: var(--white); }
  .card-back {
    top: 650px;
    background: linear-gradient(180deg, var(--brown-top), var(--brown-bottom));
  }
  .front-wave { position: absolute; inset: 0; }
  .sprig-placeholder {
    position: absolute; left: 584px; top: 162px;
    width: 82px; height: 90px; border-radius: 40px;
    background: radial-gradient(circle, var(--teal-soft) 0%, rgba(207,227,225,0) 70%);
  }
  .brand-name {
    position: absolute; left: 70px; top: 104px;
    display: flex; align-items: center; gap: 14px;
    color: var(--teal); font-weight: 500; font-size: 50px; letter-spacing: 1px;
    line-height: 1;
  }
  .brand-dot {
    width: 22px; height: 22px; border-radius: 50%; background: var(--teal);
  }
  .contact {
    position: absolute; right: 53px; top: 298px;
    text-align: right; color: var(--white);
  }
  .contact-name { font-weight: 600; font-size: 26px; line-height: 1.2; }
  .contact-title { font-size: 17px; font-weight: 500; line-height: 1.2; }
  .contact-rule {
    width: 22px; height: 2px; background: var(--white);
    margin: 12px 0 12px auto;
  }
  .contact-line { font-size: 16px; line-height: 1.35; }
  .contact-line b { font-weight: 600; }
  .promo {
    position: absolute; left: 0; right: 0; top: 140px;
    display: flex; justify-content: center; align-items: center; gap: 30px;
  }
  .promo-brand { color: var(--white); font-size: 38px; font-weight: 500; }
  .promo-offer { position: relative; width: 250px; height: 150px; }
  .promo-first {
    position: absolute; left: 80px; top: 6px;
    font-family: "Yellowtail", cursive; color: var(--white); font-size: 34px;
  }
  .promo-free {
    position: absolute; left: 0; top: 30px;
    font-family: "Yellowtail", cursive; color: var(--teal-bright);
    font-size: 110px; line-height: 1;
  }
  .tagline {
    position: absolute; left: 0; right: 0; top: 390px;
    text-align: center; color: var(--white); font-size: 19px;
  }
  .tagline .sep { color: var(--teal-bright); margin: 0 4px; }
</style>
</head>
<body>
  <section class="card card-front">
    <svg class="front-wave" viewBox="0 0 800 457" width="800" height="457">
      <path d="M325,457 C420,330 560,215 690,198 Q760,190 800,208 L800,457 Z" fill="var(--teal)"/>
    </svg>
    <div class="sprig-placeholder" role="img" aria-label="Needle and leaf sprig illustration"></div>
    <div class="brand-name"><span>NeedleNook</span><span class="brand-dot"></span></div>
    <div class="contact">
      <div class="contact-name">Coral Haskins</div>
      <div class="contact-title">MAC, L.Ac.</div>
      <div class="contact-rule"></div>
      <div class="contact-line">612-555-0193</div>
      <div class="contact-line">www.<b>needlenook-example</b>.com</div>
    </div>
  </section>

  <section class="card card-back">
    <div class="promo">
      <div class="promo-brand">NeedleNook</div>
      <div class="promo-offer">
        <span class="promo-free">free.</span>
        <span class="promo-first">first session</span>
      </div>
    </div>
    <p class="tagline">Refresh<span class="sep">•</span>Restore<span class="sep">•</span>Rejuvenate.</p>
  </section>
</body>
</html>
```